Dentistry Office

We want a new design for a Dentist's office website.

The theme is: "We provide high quality, state-of-the-art, dental care in a comfortable, caring environment."

The site currently has a menu on the left of the page with about 40 items on it. There is a great deal of textual content on each page, plus several illustrations.

We want to do this using CSS, so we need specifications in the CSS for all possible elements. The CSS needs to be named in a logical manner for easy use.

Every dentist on the planet seems to use lots of Flash. We don't want to because it is so distracting. We are looking for an elegant solution targeting 24-55 age group, but not excluding anyone.

The following (from another dentist's site) can give you a taste of what we want to communicate on the site:

"After 20 years of teaching dentists how to refine their technique and many years of writing textbooks, I currently devote my time to my office and the hands-on practice of dentistry. I'd like to welcome you personally to my dental practice, and I invite you to meet my highly experienced team of professionals.

"We have offered complete dental care of the highest quality since 1978. We provide Preventive Services, Tooth Whitening and Cosmetic Dentistry for a beautiful smile, Endodontics (root canal treatment) to treat painful teeth, Sedation Dentistry so you can relax, and Dental Implants to restore what is missing. We offer total care.

"Our approach to your health is simple: We use our education, experience and dedication to provide every patient with superior dental care.

"This passion for excellence is not just a goal, but a standard every member of our team holds.

"We also pride ourselves with our state of the art procedures, training and technology. This includes creating a beautiful smile using techniques that preserve as much of the original tooth as possible.

"Our abilities are renowned throughout the dental profession and I hope if you have any questions you will contact us by an e-mail note, by phone or just by dropping by."

Keep in mind the screen shape and dimensions. Your design needs to work in the normal screen proportions, regardless of how it looks when you post it here. Scrolling is OK, but the first impression needs to work.

Keep in mind that there will be about 250 words, or more, on each page.

Competitors web sites:

http://www.brellwickdentist.example/

http://www.brellwickdentalcare.example/

http://www.grinsbybrellwickdental.example/

http://www.dorvanfamilydentalcare.example/

http://www.brellwickdental.example/

http://www.quimbertdental.example/

We need to compete with these.

Target Market(s)

Generally adults seeking the most experienced and comfortable-to-be-with dentist.

Industry/Entity Type

Training

Requirements
Must have
• Must stand apart from other dentists.
• Must be elegant.
• Must have a horizontal menu structure across all columns, NOT a vertical that requires scrolling, no popout, pop down, etc. menus.
• We are looking for something special.
• Do not waste your time or ours putting up templates and things you have used before.
• Personally, I do not see how someone outside the US can understand the northern California dental market. But you are welcome to try.
Should not have
• Flash or graphics that move
• The look of a template
• Folksy fonts
• Looks like you used it 20 times before

```html
<!DOCTYPE html>
<html lang="en">
<head>
<meta charset="utf-8">
<title>Brellwick Dentist</title>
<link href="https://fonts.googleapis.com/css2?family=Oswald:wght@500&family=Arimo:wght@400;700&display=swap" rel="stylesheet">
<style>
:root{
  --page-bg:#dcdcdc;
  --band-top:#96a6ae;
  --band-bottom:#6e818b;
  --white:#ffffff;
  --nav-top:#fbd48a;
  --nav-bottom:#eaa640;
  --nav-line:#d49232;
  --nav-text:#2a2a2a;
  --side-top:#eef4f8;
  --side-mid:#dbe6ee;
  --side-edge:#bccdd8;
  --ink:#1a1a1a;
  --heading:#454b50;
  --sub-heading:#1c3448;
  --logo:#eef2f4;
  --hero-a:#efeeea;
  --hero-b:#e6dcd2;
  --hero-c:#c9b7a6;
  --footer-text:#ffffff;
  --footer-muted:#d7dfe3;
}
*{box-sizing:border-box;margin:0;padding:0}
html,body{width:1146px;height:1200px;overflow:hidden}
body{background:var(--page-bg);font-family:"Arimo",Arial,sans-serif;color:var(--ink);position:relative}

.site-header{position:absolute;left:0;top:0;width:1146px;height:113px;background:linear-gradient(var(--band-top),var(--band-bottom))}
.brand{position:absolute;left:57px;top:28px;font-family:"Oswald",sans-serif;font-weight:500;font-size:46px;line-height:1;color:var(--logo)}
.social{position:absolute;right:56px;top:44px;width:150px;text-align:center;color:var(--white);font-size:12px;font-weight:700}
.social-title{display:block;margin-bottom:8px}
.social-list{display:flex;justify-content:space-between;list-style:none}
.social-item{display:flex;flex-direction:column;align-items:center;font-size:9px;font-weight:400;gap:2px}
.social-dot{width:28px;height:28px;border-radius:50%;background:var(--white);opacity:.85}

.page{position:absolute;left:39px;top:113px;width:1069px;height:970px;background:var(--white)}

.main-nav{position:absolute;left:16px;top:17px;width:1037px;height:51px;border-radius:6px 6px 0 0;background:linear-gradient(var(--nav-top),var(--nav-bottom));display:flex;list-style:none}
.main-nav li{height:51px;display:flex;align-items:center;justify-content:center;font-size:17px;color:var(--nav-text);border-right:1px solid var(--nav-line)}
.main-nav li:last-child{border-right:none}

.topic-panel{position:absolute;left:16px;top:69px;width:249px;height:887px;background:linear-gradient(90deg,var(--side-mid),var(--side-top) 30%,var(--side-top) 70%,var(--side-edge))}
.topic-group{position:absolute;left:20px;width:212px}
.topic-group h3{font-size:15.5px;font-weight:700;color:var(--ink);letter-spacing:.3px;margin-bottom:6px}
.topic-links{font-size:12.3px;line-height:20.1px;color:var(--ink)}
.topic-links span+span::before{content:" · ";color:#6f7f88}

.hero{position:absolute;left:266px;top:69px;width:787px;height:275px;background:linear-gradient(90deg,var(--hero-a) 0%,var(--hero-a) 38%,var(--hero-b) 60%,var(--hero-c) 100%)}
.hero-text{position:absolute;left:20px;top:68px;color:var(--ink)}
.hero-title{font-family:"Oswald",sans-serif;font-weight:500;font-size:41px;color:var(--heading);line-height:1}
.hero-tag{font-size:14.5px;line-height:20px;margin-top:10px;width:310px}
.hero-call{font-family:"Oswald",sans-serif;font-weight:500;font-size:20px;margin-top:6px}
.hero-call strong{font-size:36px;font-weight:500;margin-left:6px}

.content{position:absolute;left:294px;top:370px;width:750px;font-size:13.4px;line-height:20.1px}
.content h1{font-size:29px;font-weight:700;color:var(--heading);line-height:32px;margin-bottom:1px}
.content p{margin-bottom:20px;width:560px}
.content p.wide{width:760px}
.content h2{font-size:13.4px;font-weight:700;color:var(--sub-heading);margin-bottom:19px}
.service-list{list-style:none;padding-left:13px;margin-bottom:20px}
.service-list li{padding-left:10px;text-indent:-10px;width:520px}
.service-list li.long{width:700px}
.service-list li::before{content:"* "}
.photo{position:absolute;border:1px solid #c8d0d5;background:linear-gradient(90deg,#f2f0ee,#d8cfc6)}
.photo-smile{left:865px;top:378px;width:188px;height:124px}
.photo-group{left:865px;top:567px;width:188px;height:131px;background:linear-gradient(90deg,#e9dccb,#b9d3dc)}

.site-footer{position:absolute;left:0;top:1083px;width:1146px;height:117px;background:linear-gradient(var(--band-bottom),var(--band-top) 60%,var(--band-bottom))}
.copyright{position:absolute;left:69px;top:27px;font-size:12px;color:var(--footer-muted)}
.footer-nav{position:absolute;left:343px;top:26px;display:flex;list-style:none;font-size:12.5px;font-weight:700;color:var(--footer-text)}
.footer-nav li+li::before{content:"/";font-weight:400;margin:0 12px}
</style>
</head>
<body>
<header class="site-header">
  <div class="brand">Brellwick Dentist</div>
  <div class="social">
    <span class="social-title">Get Social</span>
    <ul class="social-list">
      <li class="social-item"><span class="social-dot"></span>Chatline</li>
      <li class="social-item"><span class="social-dot"></span>Circlebook</li>
      <li class="social-item"><span class="social-dot"></span>Blog</li>
    </ul>
  </div>
</header>

<div class="page">
  <ul class="main-nav">
    <li style="width:156px">Home Page</li>
    <li style="width:205px">Why we are different</li>
    <li style="width:211px">Technologies we offer</li>
    <li style="width:163px">Meet Dr. Vessey</li>
    <li style="width:111px">Our Staff</li>
    <li style="width:191px">Contact Us/Links</li>
  </ul>

  <aside class="topic-panel">
    <div class="topic-group" style="top:19px">
      <h3>Education</h3>
      <p class="topic-links"><span>Emergency Dental Care</span><span>Your Mouth</span><span>Your Tooth</span><span>Cracked Tooth?</span><span>Missing a Tooth?</span><span>Sensitive Teeth</span><span>Dry Mouth</span><span>Tooth Grinding</span><span>Sleep Dentistry</span><span>Videos</span></p>
    </div>
    <div class="topic-group" style="top:281px">
      <h3>Preventative</h3>
      <p class="topic-links"><span>What is Preventive Care?</span><span>Taking Care of Your Teeth</span><span>Eating Right</span><span>Dental Check-Ups</span><span>Sealants</span><span>Periodontal Disease</span><span>Kicking the Habit</span><span>Night Guards</span><span>Dental X-Rays</span><span>Antibiotics with Treatment</span></p>
    </div>
    <div class="topic-group" style="top:543px">
      <h3>Cosmetics</h3>
      <p class="topic-links"><span>Cosmetic Dentistry</span><span>Bleaching and Whitening</span><span>Cosmetic Bonding</span><span>Esthetic Veneers</span><span>Tooth Shaping</span></p>
    </div>
    <div class="topic-group" style="top:704px">
      <h3>Restorations</h3>
      <p class="topic-links"><span>Crowns/Caps: Each Step</span><span>Porcelain Bridges</span><span>Bonded Dental Bridges</span><span>Gold Restorations</span><span>Implants</span><span>Treating Cracked Teeth</span><span>Periodontal (gum) Treatment</span></p>
    </div>
  </aside>

  <section class="hero" role="img" aria-label="Dentist in a face mask examining a smiling patient in the chair">
    <div class="hero-text">
      <div class="hero-title">Brellwick Dentist</div>
      <p class="hero-tag">Harlan Vessey, DDS, Providing Cosmetic Dentistry Excellence to Patients in Brellwick, Calden County and the Marrow Bay Area.</p>
      <p class="hero-call">Call us now: <strong>555-014-2290</strong></p>
    </div>
  </section>

  <div class="photo photo-smile" role="img" aria-label="Smiling patient seated in a dental chair"></div>
  <div class="photo photo-group" role="img" aria-label="Group of smiling young adults"></div>

  <main class="content">
    <h1>Brellwick Dentist</h1>
    <p>In Brellwick, when you're a patient of Dr. Vessey, you can be confident that you're receiving care from the most experienced, knowledgeable, and skilled cosmetic dentist in Calden County.</p>
    <p class="wide">Dr. Vessey is an award-winning leader in restorative dentistry and a genial professional.<br>His humor, dedication, and talent ensure you a pleasant experience and superb, long-lasting results.</p>
    <h2>Dr. Vessey Provides</h2>
    <ul class="service-list">
      <li>General dentistry—oral hygiene, cavity detection and repair, crowns.</li>
      <li>Cosmetic/restorative dentistry—broken or misshapen teeth, crooked smiles, unsightly gaps</li>
      <li>Non-metal fillings—nontoxic, durable tooth-colored resin fillings that are proven to provide better results</li>
      <li>Tooth shaping—extending, shortening or otherwise reshaping teeth for improved esthetics</li>
      <li class="long">Complete smile make-over's—resin veneers that reshape the whole mouth while preserving natural teeth</li>
      <li class="long">Tooth whitening—at-home bleaching options to make teeth appear years younger</li>
      <li class="long">Laser Dentistry, Sleep Dentistry, and Implant Dentistry with the Finest and Latest Equipment and Materials.</li>
      <li class="long">Dental Implants to replace missing teeth.</li>
      <li class="long">Sedation Dentistry so you can be relaxed.</li>
    </ul>
    <h2>Dr. Vessey's Commitment</h2>
    <p class="wide">After 25 years of teaching dentists how to refine their technique and many years of writing textbooks, I currently devote my time to my office and the hands-on practice of dentistry. I'd like to welcome you personally to my dental practice, and I invite you to meet my highly experienced team of professionals.</p>
  </main>
</div>

<footer class="site-footer">
  <p class="copyright">Copyright 2010. All rights reserved.</p>
  <ul class="footer-nav">
    <li>Home Page</li><li>Why we are different</li><li>Technologies we offer</li><li>Meet Dr. Vessey</li><li>Our Staff</li><li>Contact Us/Links</li>
  </ul>
</footer>
</body>
</html>
```